Web Design Project for Web Agency

WHAT I NEED:
The design I need (PSD file) is for a microsite designed for employee recruitment for Brantley, a Web agency.
***Design for the 1st Page ONLY : "Manifeste"
OBJECTIVES OF THE WEBSITE:
1. To promote the agency's corporate culture and HR management principles.
2. To get people to apply on available jobs
ELEMENTS OF THE PAGE "MANIFESTE" :
1. Brantley logo (see attached files). Beside the logo must be the word "Carrières" ("Careers" in english)
***The logo is not final and there is NO branding for Brantley yet. That is why there are multiple files. So please feel free to be creative!
2. Main menu : 4 sections
Manifeste | Opportunités | Brantly | Postuler
3. Manifeste :
This page is the home page. It will present 2 main sections :
a. The agency's corporate culture :
- Title of the page is a question : "Do you embrace Brantley's corporate culture?"
- Then, presentation of the 5 corporate values, each with a title and short description
- At the end of the list of values, we want a button that says "Apply now"
b. The agency's HR management principles :
- Title of the page is a question : "Do you see yourself working at Brantley?"
- Then, presentation of the 5 Management principles, each with a title and short description
- At the end of the list of principles, we want a button that says "Apply now"
VISUAL INSPIRATION
To create each section of the "Manifeste" page, we want a design that will fit with the corporate culture:
- Brantley is BOLD
- Brantley is PROUD
- Brantley is PROFESSIONAL
- Brantley is ELEGANT
- Brantley is REFINED
We want something slick and modern. Here are some Website's that we like that can be of inspiration:
- http://www.studio-vetrak.com/en/services
- http://quorvinpanels.com/

```html
<!DOCTYPE html>
<html lang="fr">
<head>
<meta charset="utf-8">
<title>Brantley Carrières – Manifeste</title>
<link rel="stylesheet" href="https://fonts.googleapis.com/css2?family=Arimo:wght@400;700&family=Roboto+Condensed:wght@300;400&display=swap">
<style>
  :root {
    --orange: #ee7a3b;
    --orange-soft: #f08f55;
    --rust: #d3622a;
    --burnt: #bf5323;
    --brick: #9e3a12;
    --cocoa: #7a3d28;
    --brown: #6b3420;
    --grey-text: #8a8a8a;
    --nav-text: #9a9a9a;
    --white: #ffffff;
    --footer-mark: #f3a274;
  }
  * { box-sizing: border-box; margin: 0; padding: 0; }
  html, body { width: 819px; height: 1200px; overflow: hidden; background: var(--white); }
  body { position: relative; font-family: "Arimo", Arial, sans-serif; }
  .abs { position: absolute; }

  /* Header */
  .brand-name { left: 36px; top: 18px; font-size: 52px; font-weight: 700; color: var(--orange); letter-spacing: -0.5px; line-height: 1; }
  .brand-tagline { left: 50px; top: 84px; font-size: 11.5px; letter-spacing: 4.2px; color: #444; }
  .careers-badge { left: 290px; top: 41px; width: 100px; height: 26px; background: var(--brown); border-radius: 4px; color: var(--white); font-size: 20px; font-style: italic; text-align: center; line-height: 26px; }
  .main-nav { right: 37px; top: 35px; font-size: 10px; color: var(--nav-text); display: flex; gap: 0; }
  .main-nav span { padding: 0 9px; }
  .main-nav .sep { color: var(--orange); padding: 0 6px; }
  .rule { left: 0; width: 819px; height: 3px; background: var(--orange); }

  /* Hero */
  .hero-photo { left: 0; top: 130px; width: 819px; height: 317px; background: linear-gradient(100deg, #dfe6ee 0%, #b9c4d1 30%, #6f7c8c 55%, #e9eef3 75%, #3a4352 100%); }
  .hero-callout { left: 329px; top: 318px; width: 490px; height: 52px; background: var(--orange); border-radius: 6px 0 0 6px; color: var(--white); font-family: "Roboto Condensed", sans-serif; font-size: 25px; font-weight: 400; line-height: 52px; padding-left: 36px; }
  .hero-bar { top: 426px; height: 20px; }

  /* Principles */
  .principle-photo { top: 465px; height: 110px; border: 1px solid var(--orange); border-radius: 4px; }
  .principle-title { top: 585px; font-size: 16px; line-height: 16px; }
  .principle-text { top: 623px; font-size: 9.6px; line-height: 11px; color: var(--grey-text); width: 150px; }

  .apply-button { left: 135px; top: 682px; width: 533px; height: 44px; background: var(--orange); border-radius: 6px; color: var(--white); font-size: 23px; text-align: center; line-height: 44px; }

  /* Columns */
  .column-title { top: 772px; font-size: 30px; }
  .column-text { top: 814px; width: 350px; font-size: 13px; line-height: 14.6px; color: var(--grey-text); }
  .column-text p { margin-bottom: 14px; }
  .column-divider { left: 410px; top: 775px; width: 1px; height: 228px; background: var(--orange); }

  /* Footer */
  .site-footer { left: 0; top: 1093px; width: 819px; height: 107px; background: var(--orange); overflow: hidden; }
  .footer-nav { left: 26px; top: 16px; font-size: 13px; color: var(--white); }
  .footer-contact { right: 22px; top: 16px; font-size: 13px; color: var(--white); }
  .footer-mark { right: 10px; top: 44px; font-size: 52px; font-weight: 700; color: var(--footer-mark); line-height: 1; }
</style>
</head>
<body>
  <header>
    <div class="abs brand-name">Brantley</div>
    <div class="abs brand-tagline">AGENCE NUMÉRIQUE</div>
    <div class="abs careers-badge">Carrières</div>
    <nav class="abs main-nav">
      <span>Manifeste</span><span class="sep">|</span><span>Opportunités</span><span class="sep">|</span><span>Brantly</span><span class="sep">|</span><span>Postuler</span>
    </nav>
  </header>
  <div class="abs rule" style="top:127px"></div>

  <section>
    <div class="abs hero-photo" role="img" aria-label="Photo of colleagues in suits working over documents at a bright office desk"></div>
    <h1 class="abs hero-callout">Do you embrace Brantley's corporate culture?</h1>
    <div class="abs hero-bar" style="left:9px;width:144px;background:var(--orange)"></div>
    <div class="abs hero-bar" style="left:166px;width:154px;background:var(--rust)"></div>
    <div class="abs hero-bar" style="left:333px;width:153px;background:var(--burnt)"></div>
    <div class="abs hero-bar" style="left:499px;width:154px;background:var(--brick)"></div>
    <div class="abs hero-bar" style="left:666px;width:142px;background:var(--cocoa)"></div>
  </section>
  <div class="abs rule" style="top:446px"></div>

  <section>
    <div class="abs principle-photo" style="left:9px;width:144px;background:linear-gradient(135deg,#eef0f6,#9aa3bd 60%,#2a3043)" role="img" aria-label="Paper figures of people holding hands"></div>
    <div class="abs principle-photo" style="left:165px;width:154px;background:linear-gradient(135deg,#e8e4dc,#8d7f6f 55%,#3b3631)" role="img" aria-label="Team stacking hands together"></div>
    <div class="abs principle-photo" style="left:332px;width:155px;background:radial-gradient(circle at 50% 40%,#fff27a,#f1a720 45%,#7a3a06)" role="img" aria-label="Glowing light bulb with paper figures around it"></div>
    <div class="abs principle-photo" style="left:499px;width:155px;background:linear-gradient(180deg,#f4f4f4,#d4dbe6 60%,#6f89b3)" role="img" aria-label="People holding question mark signs"></div>
    <div class="abs principle-photo" style="left:666px;width:142px;background:linear-gradient(135deg,#d9ecf7,#3d86b8 55%,#0d2d4a)" role="img" aria-label="Blue office chairs at a meeting table"></div>

    <h2 class="abs principle-title" style="left:12px;color:var(--orange);font-weight:400">Management<br>Principle 1</h2>
    <h2 class="abs principle-title" style="left:169px;color:var(--orange);font-weight:400">Management<br>Principle 2</h2>
    <h2 class="abs principle-title" style="left:337px;color:var(--burnt);font-weight:400">Management<br>Principle 3</h2>
    <h2 class="abs principle-title" style="left:506px;color:var(--brick);font-weight:400">Management<br>Principle 4</h2>
    <h2 class="abs principle-title" style="left:669px;color:var(--brown);font-weight:400">Management<br>Principle 5</h2>

    <p class="abs principle-text" style="left:12px">Lorem ipsum dolor sit amet, consectetur adipisicing elit, sed do eiusmod tempor ilit.</p>
    <p class="abs principle-text" style="left:169px">Lorem ipsum dolor sit amet, consectetur adipisicing elit, sed do eiusmod tempor ilit.</p>
    <p class="abs principle-text" style="left:337px">Lorem ipsum dolor sit amet, consectetur adipisicing elit, sed do eiusmod tempor ilit.</p>
    <p class="abs principle-text" style="left:506px">Lorem ipsum dolor sit amet, consectetur adipisicing elit, sed do eiusmod tempor ilit.</p>
    <p class="abs principle-text" style="left:670px">Lorem ipsum dolor sit amet, consectetur adipisicing elit, sed do eiusmod tempor ilit.</p>

    <a class="abs apply-button">Click here to Apply Now &gt;&gt;&gt;</a>
  </section>

  <section>
    <h2 class="abs column-title" style="left:32px;color:var(--orange);font-weight:400">Title</h2>
    <div class="abs column-text" style="left:37px">
      <p>Lorem ipsum dolor sit amet, consectetur adipisicing elit, sed do eiusmod tempor incididunt ut labore et dolore magna aliqua. Ut enim ad minim veniam, quis nostrud exercitation ullamco laboris nisi ut aliquip ex ea commodo consequat. Duis aute irure dolor in reprehenderit in v oluptate velit esse cillum dolore eu fugiat nulla pariatur.</p>
      <p>Excepteur sint occaecat cupidatat non proident, sunt in culpa qui officia deserunt mollit anim id est laborum..</p>
      <p>Excepteur sint occaecat cupidatat non proident, sunt in culpa qui officia deserunt mollit anim id est laborum.</p>
    </div>
    <div class="abs column-divider"></div>
    <h2 class="abs column-title" style="left:435px;color:var(--brown);font-weight:400">Title</h2>
    <div class="abs column-text" style="left:441px;top:812px">
      <p>Lorem ipsum dolor sit amet, consectetur adipisicing elit, sed do eiusmod tempor incididunt ut labore et dolore magna aliqua. Ut enim ad minim veniam, quis nostrud exercitation ullamco laboris nisi ut aliquip ex ea commodo consequat. Duis aute irure dolor in reprehenderit in v oluptate velit esse cillum dolore eu fugiat nulla pariatur.</p>
      <p>Excepteur sint occaecat cupidatat non proident, sunt in culpa qui officia deserunt mollit anim id est laborum.</p>
      <p>Excepteur sint occaecat cupidatat non proident, sunt in culpa qui officia deserunt mollit anim id est laborum.</p>
    </div>
  </section>

  <footer class="abs site-footer">
    <div class="abs footer-nav">Manifeste | Opportunités | Brantly | Postuler</div>
    <div class="abs footer-contact">Contact Details here</div>
    <div class="abs footer-mark">Brantley</div>
  </footer>
</body>
</html>
```